Business Card Design

New Homes
Renovations/Additions
Building Maintenance
Design
Council Approvals
Estimates
Project and Construction Management

The back of the card should only contain my logo which is attached and under the logo have written velora & velora constructions.

Industry/Entity Type

Business

Contact Information for Business Card

Company Name: Velora & Velora Constructions Pty Ltd
BLD 641372
ABN: 52 907 314 286
Position: Director
Name: Tavo Rilkenbar
Tel: m. 0418276354
f. (08)83926157
veloranvelora@mailnest.example

```html
<!DOCTYPE html>
<html lang="en">
<head>
<meta charset="utf-8">
<title>Velora &amp; Velora Constructions – Business Card</title>
<link rel="stylesheet" href="https://fonts.googleapis.com/css2?family=EB+Garamond:wght@400;600;700&display=swap">
<style>
  :root {
    --bg: #e4e6ea;
    --card-white: #ffffff;
    --brand-blue: #1a4fa8;
    --brand-blue-deep: #0f3f9e;
    --brand-blue-light: #1ea3e2;
    --text-grey: #6f6f6f;
    --rule-grey: #b9b9b9;
    --white: #ffffff;
  }
  * { margin: 0; padding: 0; box-sizing: border-box; }
  html, body { width: 1200px; height: 900px; overflow: hidden; }
  body {
    background: var(--bg);
    font-family: "EB Garamond", Georgia, serif;
    position: relative;
  }
  .card {
    position: absolute;
    width: 520px;
    height: 300px;
    border-radius: 22px;
    box-shadow: 0 10px 28px rgba(0,0,0,0.22);
    overflow: hidden;
  }

  /* Back of card */
  .card-back {
    left: 60px;
    top: 470px;
    background: radial-gradient(ellipse at 48% 42%, var(--brand-blue-light) 0%, #1677cf 45%, var(--brand-blue-deep) 100%);
    color: var(--white);
    text-align: center;
  }
  .card-back .mark {
    display: block;
    width: 78px;
    height: 78px;
    margin: 46px auto 16px;
    border: 3px solid var(--white);
    border-radius: 50%;
  }
  .card-back .wordmark {
    font-weight: 600;
    color: var(--white);
    display: inline-block;
  }
  .card-back .wordmark-main {
    display: block;
    font-size: 38px;
    letter-spacing: 1px;
    line-height: 1;
    padding-bottom: 6px;
    border-bottom: 2px solid var(--white);
  }
  .card-back .wordmark-sub {
    display: block;
    font-size: 19px;
    letter-spacing: 9px;
    margin-top: 4px;
    padding-left: 9px;
  }

  /* Front of card */
  .card-front {
    left: 620px;
    top: 130px;
    background: var(--card-white);
  }
  .brand {
    position: absolute;
    left: 30px;
    top: 26px;
    display: flex;
    align-items: center;
    gap: 10px;
    color: var(--brand-blue);
    font-weight: 700;
    font-size: 20px;
  }
  .brand .mark {
    width: 40px;
    height: 40px;
    border: 3px solid var(--brand-blue);
    border-radius: 50%;
  }
  .company {
    position: absolute;
    right: 26px;
    top: 78px;
    text-align: right;
  }
  .company-name {
    color: var(--brand-blue);
    font-weight: 700;
    font-size: 15px;
    text-transform: uppercase;
    letter-spacing: 0.3px;
  }
  .company-ids {
    color: var(--text-grey);
    font-size: 13px;
    letter-spacing: 0.3px;
  }
  .person {
    position: absolute;
    left: 30px;
    top: 118px;
  }
  .person-name {
    color: var(--brand-blue);
    font-weight: 700;
    font-size: 24px;
    line-height: 1.05;
  }
  .person-title {
    color: var(--text-grey);
    font-weight: 700;
    font-size: 15px;
  }
  .divider {
    position: absolute;
    left: 248px;
    top: 132px;
    width: 1px;
    height: 74px;
    background: var(--rule-grey);
  }
  .contacts {
    position: absolute;
    left: 264px;
    right: 26px;
    top: 126px;
    list-style: none;
  }
  .contacts li {
    display: flex;
    align-items: center;
    gap: 9px;
    height: 27px;
    color: var(--brand-blue);
    font-weight: 600;
    font-size: 14px;
    white-space: nowrap;
  }
  .contacts svg { width: 21px; height: 21px; flex: none; }
  .services {
    position: absolute;
    left: 30px;
    right: 26px;
    bottom: 26px;
    color: var(--text-grey);
    font-size: 14.5px;
    line-height: 1.35;
  }
</style>
</head>
<body>

  <section class="card card-back" aria-label="Card back">
    <span class="mark" aria-hidden="true"></span>
    <div class="wordmark">
      <span class="wordmark-main">VELORA &amp; VELORA</span>
      <span class="wordmark-sub">CONSTRUCTIONS</span>
    </div>
  </section>

  <section class="card card-front" aria-label="Card front">
    <div class="brand">
      <span class="mark" aria-hidden="true"></span>
      <span>Velora &amp; Velora</span>
    </div>

    <div class="company">
      <div class="company-name">Velora &amp; Velora Constructions Pty Ltd</div>
      <div class="company-ids">BLD: 641372 ABN: 52 907 314 286</div>
    </div>

    <div class="person">
      <div class="person-name">Tavo Rilkenbar</div>
      <div class="person-title">Managing Director</div>
    </div>

    <div class="divider"></div>

    <ul class="contacts">
      <li>
        <svg viewBox="0 0 22 22" aria-hidden="true">
          <circle cx="11" cy="11" r="10" fill="none" stroke="var(--brand-blue)" stroke-width="1.5"/>
          <path d="M7.5 6.5c.6-.6 1.3-.5 1.7.1l.9 1.4c.3.5.2 1-.2 1.4l-.5.5c.5 1.1 1.3 1.9 2.4 2.4l.5-.5c.4-.4.9-.5 1.4-.2l1.4.9c.6.4.7 1.1.1 1.7-1 1-2.5 1.2-4 .3-1.7-1-3-2.300-4-4-.9-1.5-.7-3 .3-4z" fill="var(--brand-blue)"/>
        </svg>
        <span>0418276354</span>
      </li>
      <li>
        <svg viewBox="0 0 22 22" aria-hidden="true">
          <circle cx="11" cy="11" r="10" fill="none" stroke="var(--brand-blue)" stroke-width="1.5"/>
          <rect x="6" y="9" width="10" height="6" rx="1" fill="var(--brand-blue)"/>
          <rect x="8" y="5.5" width="6" height="3.5" fill="none" stroke="var(--brand-blue)" stroke-width="1.2"/>
          <rect x="8" y="13" width="6" height="3.5" fill="var(--white)" stroke="var(--brand-blue)" stroke-width="1.2"/>
        </svg>
        <span>(08)83926157</span>
      </li>
      <li>
        <svg viewBox="0 0 22 22" aria-hidden="true">
          <circle cx="11" cy="11" r="10" fill="none" stroke="var(--brand-blue)" stroke-width="1.5"/>
          <rect x="5.5" y="7.5" width="11" height="7.5" fill="none" stroke="var(--brand-blue)" stroke-width="1.3"/>
          <path d="M5.5 7.5l5.5 4.2 5.5-4.2" fill="none" stroke="var(--brand-blue)" stroke-width="1.3"/>
        </svg>
        <span>veloranvelora@mailnest.example</span>
      </li>
    </ul>

    <p class="services">
      • New Homes • Renovations/Additions • Building Maintenance • Design<br>
      • Council Approvals • Estimates • Project and Construction Management
    </p>
  </section>

</body>
</html>
```